Corporate Two Sided Business Card

Looking for a Corporate "edgy" Modern look and feel for a business card

We are looking at two options. Dark background with our logo on it, white background with our logo on it - The background is more - Charcoal / Graphite then black

Details will be

Danielle Forsk

Licensee / Director

m. 0428 519 064

e. danielle@quorvela.com.au

quorvela.com.au

Target Market(s)

Professional Business people that refer use business and clients that own Investment Properties

Industry/Entity Type

Business

Contact Information for Business Card

Details will be

Danielle Forsk

Licensee / Director

m. 0428 519 064

quorvela.com.au

Font styles to use
Serif

Colors
000000
ec1f27
eeeeee
ffffff

Requirements
Must have
• Two options - White Background and Dark Background. - Two sided
Nice to have
• A design that is edgy, modern and new to look instead of boring style corporate cards - It should be a full integrated design
Should not have
• Block looking - Cheap.

```html
<!DOCTYPE html>
<html lang="en">
<head>
<meta charset="utf-8">
<title>Quorvela — Business Card</title>
<link rel="stylesheet" href="https://fonts.googleapis.com/css2?family=Poppins:wght@400;500;600&display=swap">
<style>
  :root {
    --graphite: #58585b;
    --graphite-dark: #3f3f42;
    --graphite-light: #6a6a6d;
    --ink: #4a4a4d;
    --red: #ec1f27;
    --paper: #ffffff;
    --mist: #eeeeee;
    --stage-top: #d6d6d6;
    --stage-bottom: #a9a9a9;
  }
  * { box-sizing: border-box; margin: 0; padding: 0; }
  html, body {
    width: 1200px;
    height: 660px;
    overflow: hidden;
  }
  body {
    background: linear-gradient(160deg, var(--stage-top), var(--stage-bottom));
    font-family: "Poppins", sans-serif;
    position: relative;
  }
  .card {
    position: absolute;
    top: 175px;
    width: 540px;
    height: 310px;
    border-radius: 26px;
    overflow: hidden;
    box-shadow: 0 8px 22px rgba(0, 0, 0, 0.28);
  }
  .card--front {
    left: 45px;
    background: linear-gradient(135deg, var(--graphite-light), var(--graphite) 50%, var(--graphite-dark));
    display: flex;
    align-items: center;
    justify-content: center;
  }
  .card--back {
    left: 615px;
    background: var(--paper);
  }
  .brand {
    display: flex;
    align-items: center;
    gap: 10px;
    font-weight: 600;
    letter-spacing: -0.5px;
    line-height: 1;
  }
  .brand__square {
    background: var(--red);
    flex: none;
  }
  .brand--front {
    font-size: 62px;
    color: var(--paper);
  }
  .brand--front .brand__square { width: 22px; height: 22px; }
  .card__shape {
    position: absolute;
    inset: 0;
    width: 100%;
    height: 100%;
  }
  .brand--back {
    position: absolute;
    left: 34px;
    top: 112px;
    font-size: 38px;
    color: var(--ink);
  }
  .brand--back .brand__square { width: 14px; height: 14px; }
  .identity {
    position: absolute;
    right: 34px;
    top: 42px;
    text-align: right;
  }
  .identity__name {
    font-size: 22px;
    font-weight: 500;
    color: var(--ink);
    line-height: 1.15;
  }
  .identity__title {
    font-size: 13px;
    font-weight: 500;
    color: var(--red);
    letter-spacing: 0.3px;
  }
  .contacts {
    position: absolute;
    left: 34px;
    bottom: 22px;
    list-style: none;
    display: flex;
    flex-direction: column;
    gap: 9px;
  }
  .contacts__item {
    display: flex;
    align-items: center;
    gap: 10px;
    font-size: 14px;
    color: var(--paper);
    letter-spacing: 0.4px;
  }
  .contacts__icon {
    width: 20px;
    height: 20px;
    border-radius: 5px;
    background: var(--red);
    display: flex;
    align-items: center;
    justify-content: center;
    flex: none;
  }
</style>
</head>
<body>

  <section class="card card--front" aria-label="Business card, front">
    <div class="brand brand--front">
      <span class="brand__square"></span>
      <span class="brand__name">quorvela</span>
    </div>
  </section>

  <section class="card card--back" aria-label="Business card, back">
    <svg class="card__shape" viewBox="0 0 540 310" aria-hidden="true">
      <defs>
        <linearGradient id="graphite-band" x1="0" y1="0" x2="1" y2="1">
          <stop offset="0" stop-color="#6a6a6d"/>
          <stop offset="0.55" stop-color="#58585b"/>
          <stop offset="1" stop-color="#404043"/>
        </linearGradient>
      </defs>
      <polygon points="0,222 540,92 540,310 0,310" fill="url(#graphite-band)"/>
      <line x1="0" y1="215" x2="540" y2="85" stroke="#ec1f27" stroke-width="2.5"/>
      <circle cx="488" cy="97.5" r="5" fill="#ec1f27" stroke="#ffffff" stroke-width="2"/>
      <line x1="0" y1="228" x2="540" y2="228" stroke="#ec1f27" stroke-width="0" />
    </svg>

    <div class="brand brand--back">
      <span class="brand__square"></span>
      <span class="brand__name">quorvela</span>
    </div>

    <div class="identity">
      <p class="identity__name">Danielle Forsk</p>
      <p class="identity__title">Licensee / Director</p>
    </div>

    <ul class="contacts">
      <li class="contacts__item">
        <span class="contacts__icon">
          <svg width="12" height="12" viewBox="0 0 12 12" aria-hidden="true">
            <rect x="3" y="0.8" width="6" height="10.4" rx="1.2" fill="none" stroke="#fff" stroke-width="1.3"/>
            <circle cx="6" cy="9.2" r="0.7" fill="#fff"/>
          </svg>
        </span>
        <span>0428 519 064</span>
      </li>
      <li class="contacts__item">
        <span class="contacts__icon">
          <svg width="12" height="12" viewBox="0 0 12 12" aria-hidden="true">
            <rect x="0.8" y="2.5" width="10.4" height="7" rx="1" fill="none" stroke="#fff" stroke-width="1.3"/>
            <polyline points="1,3 6,7 11,3" fill="none" stroke="#fff" stroke-width="1.3"/>
          </svg>
        </span>
        <span>e. danielle@quorvela.com.au</span>
      </li>
      <li class="contacts__item">
        <span class="contacts__icon">
          <svg width="12" height="12" viewBox="0 0 12 12" aria-hidden="true">
            <circle cx="6" cy="6" r="5" fill="none" stroke="#fff" stroke-width="1.2"/>
            <ellipse cx="6" cy="6" rx="2.2" ry="5" fill="none" stroke="#fff" stroke-width="1"/>
            <line x1="1" y1="6" x2="11" y2="6" stroke="#fff" stroke-width="1"/>
          </svg>
        </span>
        <span>www.quorvela.com.au</span>
      </li>
    </ul>
  </section>

</body>
</html>
```